Private Equity Company Stationary
business card, letterhead, envelope, fax cover
#46 please eliminate the email address from the envelope. Thanks
#34 Birchway Holdings Group Header and remove big logo/watermark from the center of the page.
#33 remove all the phone numbers from envelope
#21 please eliminate border (header and footer) from business card, letterhead, fax coverand just leave it plain. Please re-submit with changes
envelope flaps to remain white
The only place the cell phone number is needed is on the business card.
I need some clarification before I can submit a satifactory design.
1. Do we need to mention the name "Holdings Grouup Advisory, Inc." compulsarily in any of the media.
2. Are there any limitations on the no of colours that can be used as printing costs can vary significantly.

```html
<!DOCTYPE html>
<html lang="en">
<head>
<meta charset="utf-8">
<title>Birchway Holdings Group Stationery</title>
<link href="https://fonts.googleapis.com/css2?family=Tinos:wght@400&display=swap" rel="stylesheet">
<style>
  :root {
    --navy: #1e4476;
    --taupe: #7b7261;
    --paper: #ffffff;
    --ink-soft: #6c6c6c;
    --edge: #d4d4d4;
    --bg: #ffffff;
  }
  * { box-sizing: border-box; margin: 0; padding: 0; }
  html, body { width: 1200px; height: 1037px; overflow: hidden; background: var(--bg); }
  body { position: relative; font-family: "Tinos", "Times New Roman", serif; }
  address { font-style: normal; }

  .sheet { position: absolute; background: var(--paper); box-shadow: 0 1px 4px rgba(0,0,0,0.18); }
  .band { position: absolute; left: 0; top: 0; width: 100%; height: 100%; display: block; }

  .brand { position: absolute; display: flex; align-items: center; gap: 8px; color: var(--navy); letter-spacing: 0.03em; text-transform: uppercase; white-space: nowrap; }
  .brand-mark { background: var(--navy); flex: none; }

  .letterhead-top { left: 70px; top: 56px; width: 725px; height: 360px; }
  .letterhead-top .brand { left: 30px; top: 50px; font-size: 18px; }
  .letterhead-top .brand-mark { width: 18px; height: 18px; }

  .envelope-flap { position: absolute; left: 70px; top: 390px; width: 725px; height: 126px; display: block; filter: drop-shadow(0 -1px 2px rgba(0,0,0,0.12)); }
  .envelope { left: 70px; top: 515px; width: 725px; height: 295px; }
  .envelope .brand { left: 26px; top: 30px; font-size: 18px; }
  .envelope .brand-mark { width: 18px; height: 18px; }
  .envelope-address { position: absolute; right: 26px; bottom: 40px; color: #fff; font-size: 12px; line-height: 1.35; text-align: right; }

  .letterhead-bottom { left: 70px; top: 810px; width: 725px; height: 195px; }
  .letterhead-footer { position: absolute; right: 30px; bottom: 28px; color: #fff; font-size: 12px; line-height: 1.4; text-align: right; }

  .business-card { left: 866px; top: 560px; width: 280px; height: 170px; }
  .business-card .brand { left: 14px; top: 22px; font-size: 12px; gap: 6px; }
  .business-card .brand-mark { width: 12px; height: 12px; }
  .card-person { position: absolute; left: 16px; top: 54px; color: var(--ink-soft); line-height: 1.25; }
  .card-name { font-size: 10px; }
  .card-title { font-size: 6.5px; }
  .card-contact { position: absolute; right: 14px; bottom: 16px; color: #fff; font-size: 6px; line-height: 1.5; text-align: right; }
</style>
</head>
<body>

  <section class="sheet letterhead-top" aria-label="Letterhead">
    <div class="brand"><span class="brand-mark"></span>Birchway Holdings Group</div>
  </section>

  <svg class="envelope-flap" viewBox="0 0 725 126" aria-hidden="true">
    <path d="M18.5 8 Q20.5 0.5 30 0.5 L695 0.5 Q704.5 0.5 706.5 8 L724.5 126 L0.5 126 Z" fill="var(--paper)" stroke="var(--edge)" stroke-width="1"/>
  </svg>

  <section class="sheet envelope" aria-label="Envelope">
    <svg class="band" viewBox="0 0 725 295" preserveAspectRatio="none" aria-hidden="true">
      <polygon points="0,222 725,150 725,162 0,234" fill="var(--taupe)"/>
      <polygon points="0,240 725,168 725,295 0,295" fill="var(--navy)"/>
    </svg>
    <div class="brand"><span class="brand-mark"></span>Birchway Holdings Group</div>
    <address class="envelope-address">418 Harlow Ave, Suite 720<br>Fenwick, CA 90231</address>
  </section>

  <section class="sheet letterhead-bottom" aria-label="Letterhead footer">
    <svg class="band" viewBox="0 0 725 195" preserveAspectRatio="none" aria-hidden="true">
      <polygon points="0,44 725,4 725,16 0,56" fill="var(--taupe)"/>
      <polygon points="0,62 725,22 725,195 0,195" fill="var(--navy)"/>
    </svg>
    <address class="letterhead-footer">
      418 Harlow Ave, Suite 720, Fenwick, CA 90231<br>
      Phone: (310) 555-0142 | Fax: (310) 555-0163<br>
      www.birchwayhg.com
    </address>
  </section>

  <section class="sheet business-card" aria-label="Business card">
    <svg class="band" viewBox="0 0 280 170" preserveAspectRatio="none" aria-hidden="true">
      <polygon points="0,86 280,70 280,75 0,91" fill="var(--taupe)"/>
      <polygon points="0,94 280,78 280,170 0,170" fill="var(--navy)"/>
    </svg>
    <div class="brand"><span class="brand-mark"></span>Birchway Holdings Group</div>
    <div class="card-person">
      <div class="card-name">Elias Valmorent</div>
      <div class="card-title">Managing Director</div>
    </div>
    <address class="card-contact">
      418 Harlow Ave, Suite 720, Fenwick, CA 90231<br>
      Phone: (310) 555-0142 | Cell: (310) 555-0187 | Fax: (310) 555-0163<br>
      Email: elias@birchwayhg.com | www.birchwayhg.com<br>
      DRE #01234567
    </address>
  </section>

</body>
</html>
```